Business Card

I need a business card for my work as an energy lawyer. I am a single prctioner and I consult to energy companies regarding a variety of legal issues involving environmental matters, energy efficiency, regulations and contractual arrangements. i need a distinctive business card that stands out and is easy to read. I like bold colors or high contrast. I like a sparse architectural design. The font should be easy to read (many of my clients use reading glasses and are concerned about small type). The card should communicate that I am somewhat different from ordinary legal counsel. Below are some examples of cards that I like. Thank you for your interest and thought. Glenn Dusty Harker
Updates

Thanks to everyone who has submitted a design.  My general comments are:

1.  I like the colourful cards and the high contrast cards.
2.  I prefer the use of icons for home address, phone, mobile and email.
3.  For the high contrast cards please use three colours - black background, and red and white for the logo or information.
4.  The mobile number area code should be 403 and not 404.
5.  I also need to add a direct phone line which is 403-517-6392.

Thank you,

Glenn Harker

Reason: I have briefly extended the deadline by three days to allow those individuals who responded early to revise their designs based upon the subsequent clarification of the colours (red, white, black background) and the request to use icons and add a direct phone number.

Industry/Entity Type

Business

```html
<!DOCTYPE html>
<html lang="en">
<head>
<meta charset="utf-8">
<title>Glenn Dusty Harker – Business Card</title>
<link rel="stylesheet" href="https://fonts.googleapis.com/css2?family=Fredoka:wght@500;600&family=Quicksand:wght@500;600&display=swap">
<style>
  :root {
    --ink: #0c0c0d;
    --sky: #4ec6ee;
    --sky-deep: #36b3df;
    --paper: #ffffff;
    --backdrop: #ece8e1;
  }
  html, body {
    margin: 0;
    width: 1200px;
    height: 795px;
    overflow: hidden;
    background: var(--backdrop);
  }
  .canvas {
    position: relative;
    width: 1200px;
    height: 795px;
  }
  .card {
    position: absolute;
    top: 242px;
    width: 540px;
    height: 310px;
    border-radius: 3px;
    overflow: hidden;
    box-shadow: 0 6px 18px rgba(0,0,0,0.18);
  }
  .card--front { left: 45px; background: var(--ink); }
  .card--back  { left: 615px; background: var(--sky); }

  .name {
    position: absolute;
    margin: 0;
    font-family: "Fredoka", "Quicksand", sans-serif;
    font-weight: 600;
    color: var(--paper);
    white-space: nowrap;
    letter-spacing: 0.5px;
  }
  .title {
    position: absolute;
    margin: 0;
    font-family: "Quicksand", sans-serif;
    font-weight: 500;
    color: var(--paper);
    white-space: nowrap;
  }

  /* front */
  .card--front .name { left: 28px; top: 34px; font-size: 40px; }
  .title-band {
    position: absolute;
    left: 0; right: 0;
    top: 96px;
    height: 54px;
    background: var(--sky);
  }
  .card--front .title { left: 28px; top: 108px; font-size: 25px; }

  .contacts {
    position: absolute;
    left: 28px;
    bottom: 30px;
    margin: 0;
    display: grid;
    grid-template-columns: auto auto;
    column-gap: 12px;
    row-gap: 4px;
    font-family: "Quicksand", sans-serif;
    font-size: 16px;
  }
  .contacts dt { color: var(--sky); font-weight: 500; margin: 0; }
  .contacts dd { color: var(--paper); font-weight: 600; margin: 0; }
  .contacts dd::before { content: ":"; color: var(--paper); margin-right: 8px; }

  .address {
    position: absolute;
    right: 30px;
    top: 176px;
    margin: 0;
    font-family: "Quicksand", sans-serif;
    font-style: normal;
    font-weight: 500;
    font-size: 20px;
    line-height: 1.35;
    color: var(--sky);
    text-align: right;
  }

  /* back */
  .card--back .name { left: 40px; top: 104px; font-size: 44px; }
  .card--back .title { left: 42px; top: 166px; font-size: 26px; }
</style>
</head>
<body>
<main class="canvas">
  <section class="card card--front" aria-label="Card front">
    <h1 class="name">Glenn Dusty Harker</h1>
    <div class="title-band"></div>
    <p class="title">Barrister &amp; Solicitor, LLB, ICDD</p>
    <address class="address">2240 11th Street SW,<br>Calgary Alberta</address>
    <dl class="contacts">
      <dt>Phone</dt><dd>1.403.517.6392</dd>
      <dt>Mobile</dt><dd>1.403.628.1945</dd>
      <dt>Email</dt><dd>dusty@dustyharker.com</dd>
    </dl>
  </section>

  <section class="card card--back" aria-label="Card back">
    <h2 class="name">Glenn Dusty Harker</h2>
    <p class="title">Barrister &amp; Solicitor, LLB, ICDD</p>
  </section>
</main>
</body>
</html>
```